Business cards and stationary design

We just completed the design of our new logo and we need to print new business cards and letterhead for our nonprofit. We are looking for a fresh new design that shows off our new logo. On letterhead, we must have a column on the right or left to include our Board of Directors (up to 45 names) (see attachment)

Industry/Entity Type

Non-Profit

Contact Information for Business Card

Standard business card with name, title, Company name, mailing address phone numbers, email address and website. Tagline on back "Bringing the homeless home"

Font styles to use
Sans Serif

Requirements
Must have
• include pertinent information above
• new logo
• fonts compatible with logo
• should use logo colors only
Nice to have
• tag lines

```html
<!DOCTYPE html>
<html lang="en">
<head>
<meta charset="utf-8">
<title>Harborline Shelter Trust — Business Card</title>
<link rel="stylesheet" href="https://fonts.googleapis.com/css2?family=Michroma&family=Roboto:wght@400&display=swap">
<style>
  :root {
    --backdrop: #3a3230;
    --card: #131416;
    --card-edge: #1c1d20;
    --brand-blue: #2a8fb8;
    --brand-red: #d42a35;
    --brand-yellow: #f2b632;
    --detail-text: #c8c8c8;
    --foil-silver: #d9d9d9;
  }
  * { box-sizing: border-box; margin: 0; padding: 0; }
  html, body { width: 1200px; height: 769px; overflow: hidden; }
  body {
    background: var(--backdrop);
    font-family: "Roboto", Arial, sans-serif;
    position: relative;
  }
  .card {
    position: absolute;
    top: 236px;
    width: 525px;
    height: 300px;
    background: var(--card);
    border: 1px solid var(--card-edge);
    box-shadow: 0 14px 30px rgba(0,0,0,0.45);
  }
  .card--front { left: 50px; }
  .card--back { left: 625px; }

  .brand-mark {
    position: absolute;
    display: flex;
    align-items: center;
    gap: 10px;
    font-family: "Michroma", Arial, sans-serif;
    letter-spacing: 1px;
    text-transform: uppercase;
  }
  .brand-mark__dot {
    width: 12px; height: 12px; border-radius: 50%;
    background: var(--brand-yellow);
    flex: none;
  }
  .card--front .brand-mark {
    left: 34px; top: 150px; width: 220px;
    font-size: 15px; line-height: 1.35;
    color: var(--brand-blue);
  }
  .card--front .brand-rule {
    position: absolute; left: 34px; top: 204px;
    width: 220px; height: 2px; background: var(--brand-red);
  }

  .contact {
    position: absolute; left: 288px; top: 62px; width: 220px;
  }
  .contact__name {
    font-family: "Michroma", Arial, sans-serif;
    font-size: 17px; color: var(--brand-blue);
    letter-spacing: 1px; text-transform: uppercase;
  }
  .contact__title {
    font-family: "Michroma", Arial, sans-serif;
    font-size: 9.5px; color: var(--brand-red);
    letter-spacing: 1px; text-transform: uppercase;
    margin-top: 3px;
  }
  .contact__address {
    margin-top: 12px;
    font-size: 11.5px; line-height: 1.4; color: var(--detail-text);
  }
  .contact__lines { margin-top: 12px; list-style: none; }
  .contact__lines li {
    display: flex; align-items: center; gap: 8px;
    font-size: 11.5px; line-height: 1.6; color: var(--detail-text);
  }
  .contact__lines svg { width: 11px; height: 11px; flex: none; }

  .card--back .brand-mark {
    left: 0; right: 0; top: 112px;
    justify-content: center;
    font-size: 22px; color: var(--foil-silver);
  }
  .card--back .brand-mark__dot { background: var(--foil-silver); width: 14px; height: 14px; }
  .card--back .brand-rule {
    position: absolute; left: 92px; right: 92px; top: 168px;
    height: 1px; background: var(--foil-silver); opacity: 0.7;
  }
</style>
</head>
<body>
  <section class="card card--front" aria-label="Business card front">
    <div class="brand-mark"><span class="brand-mark__dot"></span><span>Harborline Shelter Trust</span></div>
    <div class="brand-rule"></div>

    <div class="contact">
      <p class="contact__name">Evan Carter</p>
      <p class="contact__title">CEO/Founder</p>
      <p class="contact__address">Harborline shelter trust<br>412 Willowmere Road<br>Fairbanks, Alaska 99701</p>
      <ul class="contact__lines">
        <li>
          <svg viewBox="0 0 12 12" aria-hidden="true"><path fill="#2a8fb8" d="M2.4 0.8l2 2-1 1.4c.6 1.5 1.9 2.8 3.4 3.4l1.4-1 2 2-1.3 1.8C5.6 10.4 1.6 6.4 0.6 2.1z"/></svg>
          <span>555 210 4863</span>
        </li>
        <li>
          <svg viewBox="0 0 12 12" aria-hidden="true"><rect x="0.5" y="2" width="11" height="8" fill="#2a8fb8"/><path d="M0.5 2.5L6 6.5l5.5-4" stroke="#131416" stroke-width="1.1" fill="none"/></svg>
          <span>evan@harborlinetrust.org</span>
        </li>
        <li>
          <svg viewBox="0 0 12 12" aria-hidden="true"><circle cx="6" cy="6" r="5.5" fill="#2a8fb8"/><path d="M0.8 6h10.4M6 0.6c-2.4 2.8-2.4 8 0 10.8M6 0.6c2.4 2.8 2.4 8 0 10.8" stroke="#131416" stroke-width="0.9" fill="none"/></svg>
          <span>www.harborlinetrust.org</span>
        </li>
      </ul>
    </div>
  </section>

  <section class="card card--back" aria-label="Business card back">
    <div class="brand-mark"><span class="brand-mark__dot"></span><span>Harborline Shelter Trust</span></div>
    <div class="brand-rule"></div>
  </section>
</body>
</html>
```